KLT Roofing Pty Ltd

We are a high end residential Roofing company
We would like something silimar to the attached logo with the same color scheme

Target Market(s)

High end residential Builders & Architects

Industry/Entity Type

Residential

```html
<!DOCTYPE html>
<html lang="en">
<head>
<meta charset="utf-8">
<title>Ridgeline Construction – Business Card</title>
<link href="https://fonts.googleapis.com/css2?family=Arimo:wght@400;700&display=swap" rel="stylesheet">
<style>
  :root {
    --slate: #45535e;
    --blue: #0b9ccc;
    --white: #ffffff;
    --canvas: #e9e6e1;
  }
  html, body {
    margin: 0;
    padding: 0;
    width: 1100px;
    height: 1200px;
    overflow: hidden;
    background: var(--canvas);
    font-family: "Arimo", Arial, sans-serif;
  }
  .card {
    position: absolute;
    left: 131px;
    width: 838px;
    height: 478px;
    overflow: hidden;
  }
  .card--front { top: 101px; background: var(--white); }
  .card--back { top: 621px; background: var(--slate); }

  .card__waves {
    position: absolute;
    inset: 0;
    width: 100%;
    height: 100%;
  }

  .brand {
    position: absolute;
    left: 51px;
    top: 38px;
    width: 215px;
  }
  .brand__square {
    width: 215px;
    height: 175px;
    background: var(--slate);
  }
  .brand__name {
    margin-top: 12px;
    font-size: 19px;
    font-weight: 400;
    color: var(--slate);
    white-space: nowrap;
  }

  .address {
    position: absolute;
    left: 43px;
    top: 286px;
    font-size: 21px;
    color: var(--slate);
  }

  .contact {
    position: absolute;
    right: 16px;
    top: 312px;
    text-align: right;
    color: var(--white);
  }
  .contact__name {
    font-size: 27px;
    font-weight: 700;
    line-height: 1.2;
  }
  .contact__role {
    font-size: 22px;
    line-height: 1.3;
  }
  .contact__line {
    font-size: 20px;
    line-height: 1.2;
    display: flex;
    justify-content: flex-end;
    align-items: center;
    gap: 8px;
  }
  .contact__line--phone { margin-top: 24px; }
  .contact__line--email { margin-top: 12px; }
  .contact__icon { width: 16px; height: 16px; fill: var(--white); }

  .back-name {
    position: absolute;
    inset: 0;
    display: flex;
    align-items: center;
    justify-content: center;
    text-align: center;
    white-space: nowrap;
    font-size: 54px;
    font-weight: 700;
    color: var(--white);
    letter-spacing: 1px;
  }
</style>
</head>
<body>

<section class="card card--front">
  <svg class="card__waves" viewBox="0 0 524 299" preserveAspectRatio="none" aria-hidden="true">
    <path d="M40,220 C150,250 270,235 345,165 C405,110 465,72 524,66 V299 H0 V240 Z" fill="var(--slate)"/>
    <path d="M0,196 C70,245 200,268 345,205 C290,250 200,285 120,299 L0,299 Z" fill="var(--white)"/>
    <path d="M0,205 C70,255 190,275 300,232 C240,262 150,275 0,262 Z" fill="var(--blue)"/>
    <path d="M524,76 C460,82 405,122 355,165 C330,188 310,202 290,212" fill="none" stroke="var(--white)" stroke-width="3" stroke-linecap="round"/>
  </svg>

  <div class="brand">
    <div class="brand__square"></div>
    <div class="brand__name">RIDGELINE CONSTRUCTION</div>
  </div>

  <div class="address">112 Harbour Lane, Seaview</div>

  <div class="contact">
    <div class="contact__name">Corin Maddox</div>
    <div class="contact__role">General Manager</div>
    <div class="contact__line contact__line--phone">
      <svg class="contact__icon" viewBox="0 0 24 24" aria-hidden="true"><path d="M6.6 10.8a15.1 15.1 0 0 0 6.6 6.6l2.2-2.2a1 1 0 0 1 1-.25 11.4 11.4 0 0 0 3.6.57 1 1 0 0 1 1 1V20a1 1 0 0 1-1 1A17 17 0 0 1 3 4a1 1 0 0 1 1-1h3.5a1 1 0 0 1 1 1c0 1.25.2 2.45.57 3.57a1 1 0 0 1-.25 1z"/></svg>
      <span>0400 555 018</span>
    </div>
    <div class="contact__line contact__line--email">
      <svg class="contact__icon" viewBox="0 0 24 24" aria-hidden="true"><path d="M2 5h20v14H2z M2 5l10 8 10-8" fill="var(--white)" stroke="var(--slate)" stroke-width="1.5"/></svg>
      <span>cmaddox@harbourlineroofing.com.au</span>
    </div>
  </div>
</section>

<section class="card card--back">
  <div class="back-name">RIDGELINE CONSTRUCTION</div>
</section>

</body>
</html>
```